Letterhead for New Orthopaedic Surgery Practice

My husband and I are starting our own practice named RB Spine & Vitality Center. We would like to create a nice simple but high class letterhead that doesn't use too much solid color ink when printing. I like the colors dark blue, gold, yellow. Open to other suggestions. We will need to list him and I both on the top of the letterhead. Here is the important information:
Lucinda Pryce, M.D. - Hand and Upper Extremity Surgery
Esi Dankwa, M.D. - Hip & Knee Replacement/General Orthopaedic Surgery
Location: 18735 North Bellhaven Rd
Maple Hollow, FL 33490
Phone: 954-218-4635
Fax: 954-581-2264
Email: info@myrbspine.example

The only thing is that the phone and fax numbers will change once we get into our space. I just want to get the design started. I am including several documents which are my previous practice letterhead, my current procedure room letterhead, and our new Logo. The other letterheads are just for examples but please think outside of the box! We would love to see some great designs.

Colors
0054AA
0677BA
7BADD7
CADEEF
E8F1F8
0094D4
00A9DD
6FCCEA
C7EBF8
E9F6FB

Requirements
Must have
• class, elegance, luxury

```html
<!DOCTYPE html>
<html lang="en">
<head>
<meta charset="utf-8">
<title>RB Spine &amp; Vitality Center — Letterhead</title>
<link rel="stylesheet" href="https://fonts.googleapis.com/css2?family=Montserrat:wght@300;400&family=Lato:wght@400;700&family=Satisfy&display=swap">
<style>
  :root {
    --navy: #1b2a55;
    --gold: #c9a55c;
    --ink: #1f1f1f;
    --muted: #4a4a4a;
    --paper: #ffffff;
    --backdrop: #e4e4e4;
  }
  * { box-sizing: border-box; margin: 0; padding: 0; }
  html, body { width: 1200px; height: 960px; overflow: hidden; }
  body {
    background: var(--backdrop);
    display: flex; align-items: center; justify-content: center;
  }
  .letterhead {
    position: relative;
    width: 696px; height: 900px;
    background: var(--paper);
    overflow: hidden;
    box-shadow: 0 2px 10px rgba(0,0,0,.12);
    font-family: "Lato", "Helvetica Neue", sans-serif;
    color: var(--ink);
  }
  .brand {
    position: absolute; left: 40px; top: 78px;
    display: flex; align-items: center; gap: 10px;
  }
  .brand-dot {
    width: 16px; height: 16px; border-radius: 50%;
    background: var(--navy); flex: none;
  }
  .brand-name {
    font-family: "Montserrat", sans-serif; font-weight: 400;
    font-size: 15px; letter-spacing: .04em; color: var(--navy);
    line-height: 1.3; width: 160px;
  }
  .masthead {
    position: absolute; right: 36px; top: 40px;
    display: flex; align-items: stretch; gap: 14px;
    font-family: "Montserrat", sans-serif; font-weight: 300;
    font-size: 10.5px; line-height: 1.45; color: var(--muted);
  }
  .physicians { text-align: right; }
  .physician + .physician { margin-top: 2px; }
  .masthead-divider { width: 1px; background: var(--navy); }
  .contact { list-style: none; }
  .contact li { display: flex; gap: 6px; align-items: flex-start; }
  .contact svg { width: 9px; height: 9px; margin-top: 3px; flex: none; fill: var(--navy); }
  .contact .address { margin-bottom: 4px; }
  .letter {
    position: absolute; left: 74px; top: 250px; width: 560px;
    font-size: 12.5px; line-height: 1.38;
  }
  .letter-date { margin-bottom: 16px; font-size: 13px; }
  .recipient { margin-bottom: 14px; font-size: 13px; }
  .recipient-org { margin-bottom: 14px; font-size: 13px; }
  .salutation { font-weight: 700; font-size: 15px; margin-bottom: 12px; }
  .letter-body { width: 540px; }
  .letter-body p { margin-bottom: 14px; }
  .closing { margin-top: 18px; }
  .signature {
    font-family: "Satisfy", "Brush Script MT", cursive; font-size: 32px;
    margin: 30px 0 0 60px; color: var(--ink); line-height: 1;
  }
  .swoosh { position: absolute; inset: 0; width: 100%; height: 100%; pointer-events: none; }
</style>
</head>
<body>
  <main class="letterhead">
    <div class="brand">
      <span class="brand-dot"></span>
      <span class="brand-name">RB Spine &amp; Vitality Center</span>
    </div>

    <header class="masthead">
      <div class="physicians">
        <div class="physician">Lucinda Pryce, M.D.<br>Hand and Upper Extremity Surgery</div>
        <div class="physician">Esi Dankwa, M.D.<br>Hip &amp; Knee Replacement<br>General Orthopaedic Surgery</div>
      </div>
      <span class="masthead-divider"></span>
      <ul class="contact">
        <li class="address">
          <svg viewBox="0 0 10 10"><path d="M5 0a3.5 3.5 0 0 0-3.5 3.5C1.5 6 5 10 5 10s3.5-4 3.5-6.5A3.5 3.5 0 0 0 5 0zm0 5a1.4 1.4 0 1 1 0-2.8A1.4 1.4 0 0 1 5 5z"/></svg>
          <span>18735 North Bellhaven Rd<br>Maple Hollow, FL 33490</span>
        </li>
        <li>
          <svg viewBox="0 0 10 10"><path d="M1 3c0-1 1-2 4-2s4 1 4 2v1H7V3H3v1H1zM2 5h6l1 4H1z"/></svg>
          <span>954-218-4635</span>
        </li>
        <li>
          <svg viewBox="0 0 10 10"><path d="M2 0h6v3H2zM0 3.5h10V8H8v2H2V8H0zm3 3.5v2h4V7z"/></svg>
          <span>954-581-2264</span>
        </li>
        <li>
          <svg viewBox="0 0 10 10"><path d="M0 2h10v1L5 6 0 3zm0 2l5 3 5-3v4H0z"/></svg>
          <span>info@myrbspine.example</span>
        </li>
      </ul>
    </header>

    <section class="letter">
      <p class="letter-date">January-03-2020</p>
      <p class="recipient">Mr, Tobias Wrenfield<br>President</p>
      <p class="recipient-org">Halvern Corporation<br>123 Street Name, Suite# 10<br>City, State, 120023</p>
      <p class="salutation">Dear Mr. Wrenfield</p>
      <div class="letter-body">
        <p>Lorem ipsum dolor sit amet, consectetur adipiscing elit, sed do eiusmod tempor incididunt ut labore et dolore magna aliqua. Ut enim ad minim veniam, quis nostrud exercitation ullamco laboris nisi ut aliquip ex ea commodo consequat. Duis aute irure dolor in reprehenderit in voluptate velit esse cillum dolore eu fugiat nulla pariatur.</p>
        <p>Lorem ipsum dolor sit amet, consectetur adipiscing elit, sed do eiusmod tempor incididunt ut labore et dolore magna aliqua. Ut enim ad minim veniam, quis nostrud exercitation ullamco laboris nisi ut aliquip ex ea commodo consequat. Duis aute irure dolor in reprehenderit in voluptate velit esse cillum dolore eu fugiat nulla pariatur.</p>
        <p>Lorem ipsum dolor sit amet, consectetur adipiscing elit, sed do eiusmod tempor incididunt ut labore et dolore magna aliqua. Ut enim ad minim veniam, quis nostrud exercitation ullamco laboris nisi ut aliquip ex ea commodo consequat.</p>
        <p>Excepteur sint occaecat cupidatat non proident, sunt in culpa qui officia deserunt mollit anim id est laborum. re et dolore magnam aliquam quaerat voluptatem.</p>
      </div>
      <p class="closing">Regards</p>
      <p class="signature">Marin Coleby</p>
    </section>

    <svg class="swoosh" viewBox="0 0 696 900" preserveAspectRatio="none" aria-hidden="true">
      <path fill="var(--gold)" d="M696 560 C684 640 640 695 520 755 C630 712 680 672 696 602 Z"/>
      <path fill="none" stroke="var(--navy)" stroke-width="3" d="M374 900 C420 800 510 762 600 717 C650 692 685 662 696 642"/>
      <path fill="var(--navy)" d="M396 900 C440 812 530 777 620 732 C660 712 688 688 696 674 L696 900 Z"/>
    </svg>
  </main>
</body>
</html>
```